Quorvane Limited needs a business card design

We need a business card design that reflects both professionalism and innovation and captures our brand identity. We provide online enterprise solutions to HR and executive management. We would like to use the colors in our logo (Blue and Orange). See attached file.

We would like a more creative design than the existing attached business card but maintain the same information on it.

To see our products site, please visit www.quorvane.example which reflects more our identity
Updates

Please see our site: www.quorvane.example, not www.quorvane.example.uk for our colors and look and feel

Target Market(s)

Senior Executives

Industry/Entity Type

Business

Requirements
Must have
• Logo and use of logo colors
Nice to have
• Icons
Should not have
• Images

```html
<!DOCTYPE html>
<html lang="en">
<head>
<meta charset="utf-8">
<title>Quorvane Limited – Business Card</title>
<link rel="stylesheet" href="https://fonts.googleapis.com/css2?family=Open+Sans:wght@400;600;700&display=swap">
<style>
  :root {
    --brand-blue: #0a6bb8;
    --brand-orange: #ec7424;
    --ink: #111111;
    --ink-soft: #4a4a4a;
    --card-front: #fbfbf6;
    --card-back: #e4e3dc;
    --stage-light: #d6d7dc;
    --stage-dark: #8f9096;
  }
  * { box-sizing: border-box; margin: 0; padding: 0; }
  html, body { width: 1200px; height: 1200px; overflow: hidden; }
  body {
    position: relative;
    font-family: "Open Sans", Arial, sans-serif;
    background: radial-gradient(circle at 50% 48%, var(--stage-light) 0%, #b9babf 45%, var(--stage-dark) 100%);
  }
  .card {
    position: absolute;
    left: 246px;
    width: 709px;
    height: 458px;
    border: 1px solid #7c7c80;
    box-shadow: 0 2px 8px rgba(0,0,0,0.18);
  }
  .card--front {
    top: 128px;
    background: linear-gradient(90deg, #e6e6e2 0px, var(--card-front) 70px, var(--card-front) 100%);
  }
  .card--back {
    top: 594px;
    background: radial-gradient(ellipse at 50% 50%, #fbfbf8 0%, #efeee8 40%, var(--card-back) 100%);
  }

  /* Front */
  .front-web {
    position: absolute;
    left: 20px;
    top: 118px;
    display: flex;
    flex-direction: column;
    align-items: center;
    gap: 6px;
  }
  .front-web__text {
    writing-mode: vertical-rl;
    font-size: 16px;
    color: var(--ink-soft);
    letter-spacing: 0.2px;
  }
  .front-wordmark {
    position: absolute;
    left: 64px;
    top: 76px;
    height: 306px;
    display: flex;
    align-items: center;
  }
  .front-wordmark__name {
    writing-mode: vertical-rl;
    font-weight: 400;
    font-size: 50px;
    line-height: 1;
    color: var(--ink);
    letter-spacing: 1px;
  }

  .person {
    position: absolute;
    right: 54px;
    top: 34px;
    text-align: right;
  }
  .person__name { font-weight: 700; font-size: 20px; color: var(--ink); letter-spacing: 0.3px; line-height: 1.2; }
  .person__role { font-size: 17px; color: var(--brand-orange); line-height: 1.2; }

  .company {
    position: absolute;
    right: 54px;
    top: 150px;
    font-size: 29px;
    color: var(--ink);
    letter-spacing: 0.4px;
  }
  .company strong { font-weight: 700; }

  .phones {
    position: absolute;
    right: 36px;
    top: 286px;
    display: flex;
    gap: 6px;
    align-items: flex-start;
  }
  .phones__list { list-style: none; text-align: right; font-size: 18px; line-height: 24px; color: var(--ink-soft); letter-spacing: 0.3px; }
  .phones .icon { margin-top: 4px; }

  .contact {
    position: absolute;
    left: 332px;
    top: 362px;
    font-size: 18px;
    line-height: 24px;
    color: var(--ink-soft);
    letter-spacing: 0.2px;
  }
  .contact__row { display: flex; gap: 4px; align-items: flex-start; }
  .contact__row .icon { margin-top: 4px; }

  .icon { width: 17px; height: 17px; flex: none; display: block; }

  /* Back */
  .tagline {
    position: absolute;
    top: 24px;
    width: 100%;
    text-align: center;
    font-weight: 700;
    font-size: 14px;
    color: #5a5a5a;
    letter-spacing: 0.3px;
  }
  .back-band {
    position: absolute;
    left: 70px;
    right: 70px;
    top: 132px;
    height: 176px;
    background: linear-gradient(180deg, rgba(255,255,255,0) 0%, rgba(255,255,255,0.75) 50%, rgba(255,255,255,0) 100%);
  }
  .back-wordmark {
    position: absolute;
    top: 170px;
    width: 100%;
    text-align: center;
  }
  .back-wordmark__name {
    font-weight: 400;
    font-size: 80px;
    line-height: 1;
    color: var(--ink);
    letter-spacing: 2px;
  }
  .registration {
    position: absolute;
    bottom: 22px;
    width: 100%;
    text-align: center;
    font-size: 12px;
    line-height: 20px;
    color: #5a5a5a;
    letter-spacing: 0.2px;
    text-transform: uppercase;
  }
</style>
</head>
<body>

<section class="card card--front" aria-label="Business card front">
  <div class="front-web">
    <svg class="icon" viewBox="0 0 20 20" aria-hidden="true">
      <circle cx="10" cy="10" r="9.5" fill="var(--brand-blue)"/>
      <circle cx="10" cy="10" r="6" fill="none" stroke="var(--brand-orange)" stroke-width="1.6"/>
      <ellipse cx="10" cy="10" rx="2.6" ry="6" fill="none" stroke="var(--brand-orange)" stroke-width="1.3"/>
      <line x1="4" y1="10" x2="16" y2="10" stroke="var(--brand-orange)" stroke-width="1.3"/>
    </svg>
    <span class="front-web__text">www.quorvane.example.uk</span>
  </div>

  <div class="front-wordmark">
    <span class="front-wordmark__name">Quorvane</span>
  </div>

  <div class="person">
    <p class="person__name">MARA LINDQVIST</p>
    <p class="person__role">Managing Director</p>
  </div>

  <p class="company"><strong>QUORVANE</strong> LIMITED</p>

  <div class="phones">
    <ul class="phones__list">
      <li>+44 20 7946 0321</li>
      <li>+1 323 555 0148</li>
      <li>+961 70 555 012</li>
    </ul>
    <svg class="icon" viewBox="0 0 20 20" aria-hidden="true">
      <circle cx="10" cy="10" r="9.5" fill="var(--brand-blue)"/>
      <path d="M6 5.5c1-.8 1.8-.6 2.3.4l.6 1.3c.3.7 0 1.2-.6 1.6.6 1.4 1.5 2.4 2.9 3 .4-.6 1-.9 1.6-.6l1.3.6c1 .5 1.2 1.3.4 2.3-1.6 1.6-4.2.5-6.3-1.6S4.4 7.1 6 5.5z" fill="var(--brand-orange)"/>
    </svg>
  </div>

  <div class="contact">
    <p class="contact__row">
      <svg class="icon" viewBox="0 0 20 20" aria-hidden="true">
        <circle cx="10" cy="10" r="9.5" fill="var(--brand-blue)"/>
        <rect x="4.5" y="6.5" width="11" height="7.5" rx="1" fill="var(--brand-orange)"/>
        <path d="M4.8 7l5.2 4 5.2-4" fill="none" stroke="var(--brand-blue)" stroke-width="1.1"/>
      </svg>
      <span>mlindqvist@quorvane.example.uk</span>
    </p>
    <p class="contact__row">
      <svg class="icon" viewBox="0 0 20 20" aria-hidden="true">
        <circle cx="10" cy="10" r="9.5" fill="var(--brand-blue)"/>
        <path d="M10 4.5l5.5 5h-1.6v5H11.3v-3H8.7v3H6.1v-5H4.5z" fill="var(--brand-orange)"/>
      </svg>
      <span>52 Ashcombe House,<br>118 Fenwick St, London, W1X 9QZ</span>
    </p>
  </div>
</section>

<section class="card card--back" aria-label="Business card back">
  <p class="tagline">DEVELOPING LEADERS AND ORGANISATIONS</p>
  <div class="back-band"></div>
  <div class="back-wordmark">
    <span class="back-wordmark__name">Quorvane</span>
  </div>
  <p class="registration">
    Quorvane Limited is a company registered in England &amp; Wales with company number 09371465<br>
    Registered office: Mill House, Harlow Lane, Elmsworth, Surrey, GU99 1ZZ
  </p>
</section>

</body>
</html>
```